Book cover design for the book titled "Quieter Under Lanterns."

create a book cover. The book title is, "Quieter Under Lanterns: A Ledger of Harbour Songs Across Mild Winters." The purpose of the book is to create awareness of how childhood trauma is impacting 7 out of 10 adults in the world today and that two-thirds of children will experience neglect and or abuse before their 18th birthday. One victim described that his mental and physical illness resulting from childhood trauma felt like he wa being pulled to the ground, that the force was "quieter under lanterns." The design should be clean and simple and communicate a crisis.

```html
<!DOCTYPE html>
<html lang="en">
<head>
<meta charset="utf-8">
<title>Quieter Under Lanterns — Book Cover</title>
<link rel="stylesheet" href="https://fonts.googleapis.com/css2?family=Montserrat:wght@400;600;700&display=swap">
<style>
  :root {
    --stage: #414043;
    --cover: #000000;
    --ink: #f2f2f2;
    --accent: #7fe6f2;
    --pattern-glow: rgba(120, 214, 236, 0.16);
    --pattern-soft: rgba(70, 150, 175, 0.08);
    --photo-mid: #1a2b3a;
    --photo-edge: #030507;
  }
  html, body {
    margin: 0;
    width: 1200px;
    height: 727px;
    overflow: hidden;
    background: var(--stage);
  }
  .stage {
    position: relative;
    width: 1200px;
    height: 727px;
  }
  .cover {
    position: absolute;
    left: 345px;
    top: 33px;
    width: 510px;
    height: 660px;
    background: var(--cover);
    overflow: hidden;
    box-shadow: 0 6px 18px rgba(0, 0, 0, 0.35);
    font-family: "Montserrat", sans-serif;
    color: var(--ink);
    text-align: center;
  }
  .cover-photo {
    position: absolute;
    inset: 0;
    background:
      radial-gradient(ellipse 38% 55% at 60% 45%, var(--photo-mid) 0%, rgba(10, 18, 26, 0.6) 55%, transparent 80%),
      radial-gradient(ellipse 30% 20% at 58% 82%, rgba(26, 43, 58, 0.7) 0%, transparent 80%),
      var(--photo-edge);
  }
  .cover-pattern {
    position: absolute;
    left: 0;
    right: 0;
    top: 0;
    height: 265px;
    background:
      radial-gradient(ellipse 55% 70% at 55% 30%, var(--pattern-glow) 0%, transparent 75%),
      linear-gradient(180deg, var(--pattern-soft) 0%, transparent 100%);
  }
  .title {
    position: absolute;
    left: 0;
    right: 0;
    top: 268px;
    margin: 0;
    font-weight: 700;
    line-height: 1;
  }
  .title-lead {
    display: block;
    font-size: 38px;
    font-weight: 600;
    letter-spacing: 0.3px;
  }
  .title-main {
    display: block;
    margin-top: 8px;
    font-size: 82px;
    letter-spacing: -1px;
  }
  .subtitle {
    position: absolute;
    left: 0;
    right: 0;
    top: 404px;
    margin: 0;
    font-size: 12px;
    font-weight: 700;
    letter-spacing: 1.8px;
    color: var(--accent);
  }
  .blurb {
    position: absolute;
    left: 30px;
    right: 30px;
    top: 519px;
    margin: 0;
    font-size: 10px;
    line-height: 1.36;
    font-weight: 400;
  }
  .byline {
    position: absolute;
    left: 0;
    right: 0;
    top: 592px;
    margin: 0;
    font-size: 20px;
    font-weight: 700;
  }
</style>
</head>
<body>
<main class="stage">
  <article class="cover">
    <div class="cover-photo" role="img" aria-label="Dim blue-toned photograph of a crouching figure shielding the head with one hand"></div>
    <div class="cover-pattern" role="img" aria-label="Decorative pattern of thin cyan geometric lines across the top of the cover"></div>
    <h1 class="title">
      <span class="title-lead">QUIETER UNDER</span>
      <span class="title-main">LANTERNS</span>
    </h1>
    <p class="subtitle">A LEDGER OF HARBOUR SONGS ACROSS MILD WINTERS</p>
    <p class="blurb">The purpose of the book is to create awareness of how childhood trauma is impacting 7 out of 10 adults in the world today and that two-thirds of children will experience neglect and or abuse before their 18th birthday. One victim described that his mental and physical illness resulting from childhood trauma felt like he wa being pulled to the ground, that the force was "quieter under lanterns.</p>
    <p class="byline">By. you name</p>
  </article>
</main>
</body>
</html>
```